"The Lamplighter's Ledger" book cover

Book cover for both print paperback and ebook versions of the book.
The book consists of a series of short stories (chapters) depicting various unusual stories of clients of the astrologer and personal experience of the author, a person with a professional duty to forecast future.

It should be neutral to positive. There is no restriction regarding the colors – it can be both B&W and full color.
The design should be original and not include any images which require obtaining a copyright license to use. Symbols in common use and not copyrighted are probably ok. The designer should use appropriate symbols attached in the word file.
Text for the back cover is not yet available, will be ready by the end of the project. The photos of the author for the backside are attached, please choose which you consider the best.
I will need PDF, JPEG, TIFF (all formats both in CMYK and RGB) and the source file. For CMYK, we need files with no color profiles assigned.

Target Market(s)

General

Colors

Designer to choose colors to be used in the design.

Requirements
Must have
• Please the project description
Nice to have
Should not have
• Stock images or anything else requiring additional copyright discussions and negotiations.

```html
<!DOCTYPE html>
<html lang="en">
<head>
<meta charset="utf-8">
<title>The Lamplighter's Ledger — cover wrap</title>
<link rel="stylesheet" href="https://fonts.googleapis.com/css2?family=Bebas+Neue&family=Montserrat:wght@300;400&family=Roboto:wght@400&display=swap">
<style>
  :root {
    --page-bg: #c9d1d3;
    --navy: #1f3566;
    --ink: #1b1f2a;
    --white: #ffffff;
    --sky-top: #f7f8fc;
    --lavender: #9d9ee0;
    --blue-mid: #6f98df;
    --blue-deep: #4c7fd3;
    --blue-soft: #a9c8ee;
    --mist: #e6eef6;
  }
  * { box-sizing: border-box; margin: 0; padding: 0; }
  html, body {
    width: 1200px; height: 800px; overflow: hidden;
    background: var(--page-bg);
  }
  .wrap {
    position: absolute; left: 80px; top: 30px;
    width: 1040px; height: 740px;
    display: flex;
  }
  .back-cover, .front-cover {
    position: relative; width: 500px; height: 740px; overflow: hidden;
  }
  .spine {
    position: relative; width: 40px; height: 740px;
    background: linear-gradient(180deg, var(--mist) 0%, var(--blue-soft) 45%, var(--blue-mid) 80%, var(--blue-soft) 100%);
  }
  .art {
    position: absolute; inset: 0;
  }
  .back-cover .art {
    background:
      radial-gradient(ellipse at 80% 40%, rgba(111,152,223,.55), transparent 55%),
      radial-gradient(ellipse at 30% 75%, rgba(76,127,211,.6), transparent 60%),
      linear-gradient(180deg, var(--mist) 0%, #d9e0f2 22%, var(--blue-soft) 55%, var(--blue-mid) 80%, var(--mist) 100%);
  }
  .front-cover .art {
    background:
      radial-gradient(ellipse at 50% 55%, rgba(157,158,224,.7), transparent 55%),
      linear-gradient(180deg, var(--sky-top) 0%, #cfd3f1 22%, var(--lavender) 42%, var(--blue-mid) 62%, var(--blue-deep) 80%, var(--blue-soft) 94%, var(--white) 100%);
  }

  /* Front */
  .front-author {
    position: absolute; top: 160px; width: 100%; text-align: center;
    font: 300 44px/1 'Montserrat', sans-serif; color: var(--navy);
  }
  .front-title {
    position: absolute; top: 300px; width: 100%; text-align: center;
    font: 400 86px/0.98 'Bebas Neue', sans-serif; color: var(--white);
    letter-spacing: 1px;
  }
  .front-subtitle {
    position: absolute; top: 585px; width: 100%; text-align: center;
    font: 400 26px/1.25 'Montserrat', sans-serif; color: var(--navy);
  }
  .front-translator {
    position: absolute; bottom: 34px; width: 100%; text-align: center;
    font: 400 21px/1 'Montserrat', sans-serif; color: var(--ink);
    letter-spacing: 2px;
  }

  /* Spine */
  .spine-title, .spine-author {
    position: absolute; left: 50%;
    writing-mode: vertical-rl; transform: translateX(-50%);
    white-space: nowrap;
  }
  .spine-title {
    top: 30px; font: 400 24px/1 'Bebas Neue', sans-serif; color: var(--navy); letter-spacing: 1px;
  }
  .spine-author {
    bottom: 40px; font: 400 15px/1 'Montserrat', sans-serif; color: var(--navy);
  }

  /* Back */
  .back-title {
    position: absolute; top: 32px; width: 100%; text-align: center;
    font: 400 44px/1 'Bebas Neue', sans-serif; color: var(--navy); letter-spacing: 1px;
  }
  .back-subtitle {
    position: absolute; top: 80px; width: 100%; text-align: center;
    font: 400 16px/1 'Montserrat', sans-serif; color: var(--navy);
  }
  .back-blurb, .author-bio, .author-bio-cont {
    position: absolute;
    font: 400 12.6px/1.42 'Roboto', sans-serif; color: var(--ink);
  }
  .back-blurb { top: 120px; left: 30px; width: 440px; }
  .author-photo {
    position: absolute; top: 478px; left: 34px; width: 88px; height: 100px;
    background: linear-gradient(160deg, #f1e3cf 0%, #e7cdb2 45%, #f4f2ee 100%);
  }
  .author-name {
    position: absolute; top: 488px; left: 140px;
    font: 400 30px/1 'Montserrat', sans-serif; color: var(--navy);
  }
  .author-bio { top: 530px; left: 140px; width: 330px; }
  .author-bio-cont { top: 592px; left: 34px; width: 436px; }
</style>
</head>
<body>
  <main class="wrap">
    <section class="back-cover">
      <div class="art" role="img" aria-label="Soft blue watercolour wash background"></div>
      <h2 class="back-title">The Lamplighter's Ledger</h2>
      <p class="back-subtitle">Real-life stories on how the stars shapes our lives</p>
      <p class="back-blurb">Book cover for both print paperback and ebook versions of the book. &lt;br/&gt;The book consists of a series of short stories (chapters) depicting various unusual stories of clients of the astrologer and personal experience of the author, a person with a professional duty to forecast future. &lt;br/&gt;&lt;br/&gt;I attached a sketch of the cover. Please consider the sketch as an idea – do not reuse it. &lt;br/&gt;&lt;br/&gt;The main idea – stars (in form of astrological symbols) falling from the above smear, spread over and form images of basic emotions and – love, grief, happiness, fear, ecstasy, jealousy etc. Images, like patterns in coffee cup reading, should be easily identified by the reader. You can use the watercolor effect for this. The sketch looks a bit mournfully but I do not want the cover to have this impression. It should be neutral to positive. There is no restriction regarding the colors – it can be both B&amp;W and full color. &lt;br/&gt;The design should be original and not include any images which require obtaining a copyright license to use. Symbols in common use and not copyrighted are probably ok. The designer should use appropriate symbols attached in the word file. &lt;br/&gt;Text for the back cover is not yet available, will be ready by the end of the project. The photos of the author for the backside are attached, please choose which you consider the best. &lt;br/&gt;I will need PDF, JPEG, TIFF (all formats both in CMYK and RGB) and the source file. For CMYK, we need files with no color profiles assigned. &lt;br/&gt;</p>
      <div class="author-photo" role="img" aria-label="Author portrait photograph"></div>
      <h3 class="author-name">Vera Lindqvist</h3>
      <p class="author-bio">There is no restriction regarding the colors – it can be both B&amp;W and full color. &lt;br/&gt;The design should be original and not include any images which require obtaining a copyright</p>
      <p class="author-bio-cont">license to use. Symbols in common use and not copyrighted are probably ok. The designer should use appropriate symbols attached in the word file. &lt;br/&gt;Text for the back cover is not yet available, will be ready by the end of the project. The photos of the author for the backside are attached, please choose which you consider the best. &lt;br/&gt;I will need PDF, JPEG, TIFF (all formats both in CMYK and RGB) and the source file. For CMYK, we need files with no color profiles assigned. &lt;br/&gt;</p>
    </section>

    <section class="spine">
      <span class="spine-title">The Lamplighter's Ledger</span>
      <span class="spine-author">Vera Lindqvist</span>
    </section>

    <section class="front-cover">
      <div class="art" role="img" aria-label="Watercolour illustration of stars falling from above into blue and violet silhouettes of people showing emotions"></div>
      <p class="front-author">Vera Lindqvist</p>
      <h1 class="front-title">The<br>Lamplighter's<br>Ledger</h1>
      <p class="front-subtitle">Real-life stories on how<br>the stars shapes our lives</p>
      <p class="front-translator">Translated by Miriam Hale</p>
    </section>
  </main>
</body>
</html>
```